New Architectural Firm Business Cards

New Business card to compliment previous pixel forum logo (attached). Please design a business card that is simple, modern, creative....please do not use "symbols", simply the logo and associated graphics/text. The front should contain name/address/phone/email/web address (with graphics).....back should be 100% graphic design using the logo somehow. Hoping for a two color (black and yellow) design. full bleed design, no borders

Target Market(s)

Commercial Architecture Clients

Industry/Entity Type

Architecture

Contact Information for Business Card

Please design a business card that is simple, modern, creative....please do not use "symbols", simply the logo and associated graphics/text. The front should contain name/address/phone/email/web address (with graphics).....back should be 100% graphic design using the logo somehow

Font styles to use
Sans Serif

Colors
FFF300
FFF600
FEFA6F
FFFEC7
FFFEE8

Requirements
Must have
• Clean, Modern Design
Should not have
• Stock images or "icons"

```html
<!DOCTYPE html>
<html lang="en">
<head>
<meta charset="utf-8">
<title>Kestrel Architecture – Business Card</title>
<link href="https://fonts.googleapis.com/css2?family=Montserrat:wght@400;500;700&display=swap" rel="stylesheet">
<style>
  :root {
    --backdrop: #242424;
    --card-light: #eceded;
    --card-light-edge: #e3e4e5;
    --card-dark: #1b1a1a;
    --brand-yellow: #e3b814;
    --ink: #2a2a2a;
    --paper-white: #f4f4f4;
    --ghost: rgba(255, 255, 255, 0.45);
  }
  * { box-sizing: border-box; margin: 0; padding: 0; }
  html, body {
    width: 1200px;
    height: 1200px;
    overflow: hidden;
    background: var(--backdrop);
    font-family: "Montserrat", sans-serif;
  }
  .stage {
    position: relative;
    width: 1200px;
    height: 1200px;
  }
  .card {
    position: absolute;
    left: 227px;
    width: 746px;
    height: 425px;
    overflow: hidden;
  }
  .card--front {
    top: 135px;
    background: linear-gradient(135deg, var(--paper-white) 0%, var(--card-light) 60%, var(--card-light-edge) 100%);
  }
  .card--back {
    top: 640px;
    background: var(--card-dark);
  }
  .ghost-disc {
    position: absolute;
    left: 358px;
    top: 35px;
    width: 270px;
    height: 270px;
    border-radius: 50%;
    background: var(--ghost);
  }
  .wordmark {
    display: flex;
    align-items: center;
    gap: 12px;
    color: var(--brand-yellow);
    font-weight: 700;
    line-height: 1.02;
    text-transform: uppercase;
  }
  .wordmark__square {
    flex: none;
    background: var(--brand-yellow);
  }
  .card--front .wordmark {
    position: absolute;
    left: 41px;
    top: 68px;
    font-size: 34px;
    letter-spacing: 0.5px;
  }
  .card--front .wordmark__square { width: 58px; height: 58px; }
  .person {
    position: absolute;
    left: 41px;
    top: 238px;
  }
  .person__name {
    color: var(--brand-yellow);
    font-weight: 700;
    font-size: 25px;
    letter-spacing: 0.3px;
    text-transform: uppercase;
  }
  .person__role {
    color: var(--ink);
    font-size: 19px;
    margin-top: 2px;
  }
  .rule {
    position: absolute;
    left: 41px;
    top: 310px;
    width: 56px;
    height: 3px;
    background: var(--brand-yellow);
  }
  .contact {
    position: absolute;
    left: 40px;
    top: 332px;
    color: var(--ink);
    font-size: 18px;
  }
  .contact__line + .contact__line { margin-top: 13px; }
  .contact__label { color: var(--brand-yellow); }
  .contact__sep { color: var(--brand-yellow); margin: 0 10px; }
  .card--back .wordmark {
    position: absolute;
    left: 0;
    right: 0;
    top: 130px;
    justify-content: center;
    font-size: 44px;
    gap: 16px;
  }
  .card--back .wordmark__square { width: 90px; height: 90px; }
  .web {
    position: absolute;
    left: 0;
    right: 0;
    top: 358px;
    text-align: center;
    color: var(--paper-white);
    font-size: 19px;
    letter-spacing: 0.3px;
  }
</style>
</head>
<body>
  <main class="stage">
    <section class="card card--front">
      <div class="ghost-disc" aria-hidden="true"></div>
      <div class="wordmark">
        <span class="wordmark__square"></span>
        <span>Kestrel<br>Architecture</span>
      </div>
      <div class="person">
        <p class="person__name">Marcus Hale</p>
        <p class="person__role">Principal Architect</p>
      </div>
      <div class="rule"></div>
      <div class="contact">
        <p class="contact__line">Unit 12 Harbour Yard, 8 Linden Road, London, N4 7QT</p>
        <p class="contact__line"><span class="contact__label">p.</span> +44 (0) 20 7000 4821<span class="contact__sep">|</span><span class="contact__label">e.</span> studio@kestrelarch.com</p>
      </div>
    </section>

    <section class="card card--back">
      <div class="wordmark">
        <span class="wordmark__square"></span>
        <span>Kestrel<br>Architecture</span>
      </div>
      <p class="web">www.kestrelarch.com</p>
    </section>
  </main>
</body>
</html>
```